Business card for a plastic surgeon

i need a business card for a plastic surgeon. I have two adresses. The card should communicate safety, simmetry, beauty and with soft colors.
What i want in the card:
- my logo: Letters "R"and "B" (picture uploaded)
- my name: Renato Bastiani
- my registration: CRM 507 219
- my adresses and phone numbers (2):
- Av Dr Teixeira Lopes, 2710, sala 305 - Vila Olímpia | São Paulo/ SP - Phone: 11 4172-5036
- Al. Itapeva, 47, 3 andar - Alphaville | Barueri/ SP - Phone: 11 6350-2481

- my social network: site, facebook and instagram

Target Market(s)

people (95% girls and women) that want cosmetic procedures and plastic surgery

Industry/Entity Type

Business

Contact Information for Business Card

The card should communicate safety, simmetry, beauty and with soft colors.
Beige, brown, gray, rosy are some options. Color is free

Font styles to use
Serif

Requirements
Must have
• - my logo: Letters "R"and "B" (picture uploaded)
• - my name: Renato Bastiani
• - my registration: CRM 507 219
• - my adresses and phone numbers (2):
• - Av Dr Teixeira Lopes, 2710, sala 305 - Vila Olímpia | São Paulo/ SP - Phone: 11 4172-5036
• - Al. Itapeva, 47, 3 andar - Alphaville | Barueri/ SP - Phone: 11 6350-2481
• - my social network: site, facebook and instagram
Should not have
• other images (only my logo)

```html
<!DOCTYPE html>
<html lang="pt-BR">
<head>
<meta charset="utf-8">
<title>Cartão de visita — Dr. Renato Bastiani</title>
<link href="https://fonts.googleapis.com/css2?family=Cinzel:wght@400&family=Montserrat:wght@400;700&display=swap" rel="stylesheet">
<style>
  :root{
    --page:#ece9e6;
    --peach:#f4b8a4;
    --brown:#7a4a44;
    --mist:#d9dde2;
    --slate:#6b7798;
    --teal:#75999a;
    --white:#ffffff;
  }
  *{box-sizing:border-box;margin:0;padding:0}
  html,body{width:1200px;height:826px;overflow:hidden;background:var(--page)}
  .canvas{position:relative;width:1200px;height:826px}
  .card{position:absolute;width:540px;height:300px;background:var(--peach);
        box-shadow:0 6px 18px rgba(60,40,35,.18)}
  .card--info{left:40px;top:110px}
  .card--brand{left:620px;top:410px}

  .framed{position:absolute;background:var(--mist);border:6px solid var(--brown)}
  .logo-box{left:12px;top:12px;width:178px;height:182px;
            display:flex;flex-direction:column;align-items:center;justify-content:center;gap:10px}
  .name-box{left:200px;top:12px;width:328px;height:50px;padding:4px 0 0 26px}
  .links-box{left:200px;top:70px;width:328px;height:108px;padding:14px 0 0 22px}

  .doctor-name{font-family:'Montserrat',sans-serif;font-weight:700;font-size:20px;color:var(--brown);line-height:1}
  .crm{font-family:'Montserrat',sans-serif;font-size:12px;color:var(--brown);margin-left:118px;margin-top:1px}

  .link{display:flex;align-items:center;gap:12px;font-family:'Montserrat',sans-serif;
        font-size:12px;color:var(--brown);height:26px}
  .link svg{flex:none}

  .address{position:absolute;color:var(--white);font-family:'Montserrat',sans-serif;
           font-size:12.5px;line-height:1.35;padding:16px 0 0 26px}
  .address--sp{left:0;top:204px;width:266px;height:96px;background:var(--slate)}
  .address--alpha{left:276px;top:186px;width:264px;height:100px;background:var(--teal)}
  .phone{display:flex;align-items:center;gap:7px;margin-top:2px}

  .wordmark{font-family:'Cinzel',serif;font-weight:400;color:var(--brown);text-align:center}
  .logo-box .wordmark{font-size:13px;line-height:1.2}
  .mark-dot{width:16px;height:16px;border-radius:50%;background:var(--brown)}

  .brand-frame{position:absolute;left:26px;top:26px;width:488px;height:248px;
               background:var(--mist);border:6px solid var(--brown);
               display:flex;flex-direction:column;align-items:center;justify-content:center;gap:16px}
  .brand-frame .wordmark{font-size:26px;letter-spacing:1px}
  .brand-frame .mark-dot{width:26px;height:26px}
</style>
</head>
<body>
<main class="canvas">

  <section class="card card--info" aria-label="Verso do cartão">
    <div class="framed logo-box">
      <span class="mark-dot"></span>
      <span class="wordmark">Dr. Renato<br>Bastiani</span>
    </div>

    <div class="framed name-box">
      <p class="doctor-name">Renato Bastiani</p>
      <p class="crm">CRM 507 219</p>
    </div>

    <div class="framed links-box">
      <p class="link">
        <svg width="16" height="16" viewBox="0 0 16 16" fill="none" stroke="#7a4a44" stroke-width="1.4">
          <circle cx="8" cy="8" r="6.5"/><ellipse cx="8" cy="8" rx="3" ry="6.5"/>
          <line x1="1.5" y1="8" x2="14.5" y2="8"/>
        </svg>
        http://www.rbclinica.com
      </p>
      <p class="link">
        <svg width="16" height="16" viewBox="0 0 16 16"><circle cx="8" cy="8" r="6.5" fill="none" stroke="#7a4a44" stroke-width="1.4"/></svg>
        www.lumigram.com/
      </p>
      <p class="link">
        <svg width="16" height="16" viewBox="0 0 16 16"><circle cx="8" cy="8" r="6.5" fill="none" stroke="#7a4a44" stroke-width="1.4"/></svg>
        pageshare.com
      </p>
    </div>

    <address class="address address--sp">
      Av Dr Teixeira Lopes, 2710<br>
      sala 305 - Vila Olímpia<br>
      São Paulo/ SP
      <span class="phone">
        <svg width="16" height="16" viewBox="0 0 16 16" fill="none" stroke="#fff" stroke-width="1.3">
          <circle cx="8" cy="8" r="6.8"/>
          <path d="M5.6 4.8l1.3 1.4-.7 1a4.5 4.5 0 0 0 2.3 2.3l1-.7 1.4 1.3-.8 1.1c-2.6-.4-4.6-2.4-5-5z"/>
        </svg>
        11 4172-5036
      </span>
    </address>

    <address class="address address--alpha">
      Al. Itapeva, 47, 3 andar<br>
      Alphaville<br>
      Barueri/ SP
      <span class="phone">
        <svg width="16" height="16" viewBox="0 0 16 16" fill="none" stroke="#fff" stroke-width="1.3">
          <circle cx="8" cy="8" r="6.8"/>
          <path d="M5.6 4.8l1.3 1.4-.7 1a4.5 4.5 0 0 0 2.3 2.3l1-.7 1.4 1.3-.8 1.1c-2.6-.4-4.6-2.4-5-5z"/>
        </svg>
        11 6350-2481
      </span>
    </address>
  </section>

  <section class="card card--brand" aria-label="Frente do cartão">
    <div class="brand-frame">
      <span class="mark-dot"></span>
      <span class="wordmark">Dr. Renato Bastiani</span>
    </div>
  </section>

</main>
</body>
</html>
```